design a gift card and hanger backing for our saddlery

need a design for a pvc gift card (business card size) for our saddlery and if possible a back card board hanger. front to have a nice design and 'Gift Card' back of card to have our details supplied below. i will upload some pictures and logos but happy for them to be or not be used open to suggestions for designs

Target Market(s)

horse lovers of all ages and disaplines

Industry/Entity Type

Equestrian Supplies/Retail

Contact Information for Business Card

on the back - Larkmoor Horse Supplies www.larkmoors.example.au 1300 48 27 96 -and a signature panel (we will stick a code here)

Requirements
Must have
• horse themed
Nice to have
• open to all ideas
Should not have
• logo as main picture or on front

```html
<!DOCTYPE html>
<html lang="en">
<head>
<meta charset="utf-8">
<title>Larkmoor Horse Supplies – Gift Card</title>
<link rel="stylesheet" href="https://fonts.googleapis.com/css2?family=Source+Serif+4:wght@400&family=Open+Sans:wght@500&display=swap">
<style>
  :root {
    --page-bg: #f1f2f2;
    --card-navy: #1b3966;
    --horse-blue: #2f86cf;
    --horse-blue-soft: #1f5f9e;
    --brand-gold: #eeb422;
    --text-white: #ffffff;
    --panel-white: #ffffff;
  }
  * { margin: 0; padding: 0; box-sizing: border-box; }
  html, body {
    width: 1200px;
    height: 1200px;
    overflow: hidden;
    background: var(--page-bg);
  }
  .canvas {
    position: relative;
    width: 1200px;
    height: 1200px;
  }
  .card {
    position: absolute;
    left: 87px;
    width: 979px;
    background: var(--card-navy);
    border-radius: 33px;
    box-shadow: 0 6px 18px rgba(0, 0, 0, 0.12);
    overflow: hidden;
  }
  .card--front { top: 54px; height: 544px; }
  .card--back { top: 633px; height: 527px; }

  .front-illustration {
    position: absolute;
    left: 42px;
    top: 37px;
    width: 363px;
    height: 460px;
  }
  .gift-title {
    position: absolute;
    left: 538px;
    top: 112px;
    font-family: "Source Serif 4", Georgia, serif;
    font-weight: 400;
    font-size: 190px;
    line-height: 155px;
    color: var(--text-white);
    letter-spacing: -2px;
  }
  .gift-title span { display: block; }

  .brand-mark {
    position: absolute;
    left: 42px;
    top: 62px;
    display: flex;
    align-items: center;
    gap: 16px;
  }
  .brand-mark__dot {
    width: 34px;
    height: 34px;
    border-radius: 50%;
    background: var(--brand-gold);
  }
  .brand-mark__name {
    font-family: "Source Serif 4", Georgia, serif;
    font-weight: 400;
    font-size: 64px;
    line-height: 1;
    color: var(--brand-gold);
  }
  .business-name {
    position: absolute;
    left: 48px;
    top: 252px;
    font-family: "Source Serif 4", Georgia, serif;
    font-weight: 400;
    font-size: 70px;
    line-height: 79px;
    color: var(--text-white);
  }
  .business-name span { display: block; }
  .phone {
    position: absolute;
    left: 48px;
    top: 441px;
    font-family: "Open Sans", Arial, sans-serif;
    font-weight: 500;
    font-size: 41px;
    line-height: 1;
    color: var(--text-white);
  }
  .signature-panel {
    position: absolute;
    left: 581px;
    top: 410px;
    width: 359px;
    height: 85px;
    background: var(--panel-white);
    border-radius: 7px;
  }
</style>
</head>
<body>
<main class="canvas">
  <section class="card card--front">
    <svg class="front-illustration" role="img" aria-label="Flowing line illustration of a horse head with a windswept mane" viewBox="0 0 363 460">
      <defs>
        <linearGradient id="horseTone" x1="0" y1="0" x2="1" y2="1">
          <stop offset="0" stop-color="var(--horse-blue)" stop-opacity="0.55"/>
          <stop offset="1" stop-color="var(--horse-blue-soft)" stop-opacity="0.35"/>
        </linearGradient>
      </defs>
      <rect width="363" height="460" rx="24" fill="url(#horseTone)"/>
    </svg>
    <h1 class="gift-title"><span>Gift</span><span>Card</span></h1>
  </section>

  <section class="card card--back">
    <div class="brand-mark">
      <span class="brand-mark__dot"></span>
      <span class="brand-mark__name">Larkmoor</span>
    </div>
    <h2 class="business-name"><span>Larkmoor Horse</span><span>Supplies</span></h2>
    <p class="phone">1300 48 27 96</p>
    <div class="signature-panel"></div>
  </section>
</main>
</body>
</html>
```